Wordpress Design for a website design company

Web Design for a Web Design Company - As odd as that sounds, it is exactly right. We are a website design company with over 120 regular clients, we want to redesign our current website and take it to the next level. The problem we are finding is that we are too "inside the box". Which is why we are looking outside for a designer that will take us to the next level. We need this design to look STATE OF THE ART! Obviously there is allot we can do internally once we have a completed design to wrap up the project. So what we are looking for are some design concepts based on some ideas that we will provide. Once the concept is finalized we will need the layered design and any graphics that were used in separate files. If you have any questions please send them to us privately.

Example websites of how we want to look are:

1. http://www.brivlo.example
2. http://www.tealkettle.example
3. http://vunmorefolio.example
4. http://www.zup.example
5. http://www.palvextra.example

Our current website we are redesigning is: www.hurnlatewd.example

Navigation / Pages for new website are as follows:

Home
Services (page with broad detailing)
Portfolio
RFQ
Testimonials
About
Contact

Website Design
Website Re-design
Ecommerce
Mobile Websites
Copywriting
Hosting and Maintenance
Content Marketing
Pay Per Click Marketing
Mobile Text Marketing
Local Search Marketing

Design must be wordpress compatible, we use the kestrel framework specifically.
Target Market(s)
Our target market is B2B, we want to sell web and marketing products
Requirements
Must Have:
- Design must be wordpress compatible, we use the kestrel framework specifically.

As a bonus, if we like your work we may use you for our own clients...
Updates

Project has been made guaranteed, please let me know if you have any questions...

Marcus

Reason: Did not want to end on a weekend to make sure all submissions are in.

Industry/Entity Type

Marketing

Requirements
Must have
• For the content area - intro paragraph and blog categories below the header/banner area,

Need to include both shaded content "buttons" with graphics similar to the website attached jpg file titled - bottom content area

and hanging shaded ribbons from plimbart.example - attached jpg file titled: stock-illustration-57302618-glossy-promoting-badges

```html
<!DOCTYPE html>
<html lang="en">
<head>
<meta charset="utf-8">
<title>Hurnlate Website Design</title>
<link rel="stylesheet" href="https://fonts.googleapis.com/css2?family=Open+Sans:ital,wght@0,300;0,400;0,600;0,700;1,400&family=Arimo:wght@400;700&family=Great+Vibes&display=swap">
<style>
:root{
  --blue:#1ea0e0;
  --blue-dark:#0a6fb8;
  --orange:#f39a1d;
  --orange-deep:#e8821a;
  --yellow:#f7c21a;
  --cream:#fdf1b6;
  --text:#8a8a8a;
  --text-dark:#555;
  --nav:#777;
  --footer-bg:#efefef;
  --white:#fff;
}
*{margin:0;padding:0;box-sizing:border-box}
html,body{width:1200px;height:2595px;overflow:hidden;background:var(--white)}
body{position:relative;font-family:"Arimo",Arial,sans-serif;color:var(--text)}
h1,h2,h3,h4{font-weight:400}
.abs{position:absolute}
a{color:inherit;text-decoration:none}

/* header */
.topline{left:0;top:0;width:1200px;height:4px;background:var(--yellow)}
.site-header{left:0;top:4px;width:1200px;height:66px;background:var(--white)}
.nav-item{top:26px;font-family:"Open Sans",sans-serif;font-size:13px;color:var(--nav);text-transform:uppercase}
.nav-item.active{color:var(--blue)}
.nav-active-bar{left:248px;top:63px;width:70px;height:5px;background:var(--blue)}
.logo-tab{left:502px;top:0;width:196px;height:108px;background:var(--white);border-radius:0 0 98px 98px;z-index:2;text-align:center}
.logo-name{padding-top:50px;font-family:"Open Sans",sans-serif;font-weight:600;font-size:18px;letter-spacing:2px;color:var(--text-dark)}

/* hero */
.hero{left:0;top:70px;width:1200px;height:395px;background:linear-gradient(180deg,#c9b79a 0%,#e8c27a 40%,#d9a55a 62%,#8c8a4a 100%)}
.hero-arrow{width:62px;height:62px;border-radius:50%;border:2px solid rgba(255,255,255,.85)}

/* intro */
.intro-title{left:0;top:508px;width:1200px;text-align:center;font-family:"Open Sans",sans-serif;font-size:22px;color:var(--blue)}
.intro-text{left:235px;top:547px;width:730px;text-align:center;font-size:13px;line-height:19px;color:var(--text)}

/* feature cards */
.card{top:625px;width:270px;height:132px;overflow:hidden}
.card h3{font-family:"Open Sans",sans-serif;font-size:21px;color:var(--white);text-align:center;padding-top:12px}
.card-yellow{left:173px;background:linear-gradient(180deg,#fbc21b,#f7a70f)}
.card-orange{left:465px;background:linear-gradient(180deg,#f89a1c,#e6761a)}
.card-blue{left:757px;background:linear-gradient(180deg,#1fa3ea,#0f72c9)}
.card-art{position:absolute;left:12px;top:56px;width:246px;height:76px;background:linear-gradient(180deg,#f4f4f4,#d6d6d6)}

/* portfolio */
.portfolio{left:0;top:832px;width:1200px;height:543px;background:radial-gradient(ellipse at 50% 40%,#f8a430 0%,var(--orange-deep) 100%)}
.portfolio-title{left:0;top:870px;width:1200px;text-align:center;font-family:"Open Sans",sans-serif;font-weight:300;font-size:60px;color:var(--white)}
.portfolio-item{top:1005px;width:270px;height:225px;background:linear-gradient(180deg,#f3e3b0,#d9d9d9)}
.view-all{left:0;top:1255px;width:1200px;text-align:center;font-family:"Great Vibes",cursive;font-size:52px;color:var(--white)}
.view-all-line{left:520px;top:1322px;width:170px;height:2px;background:var(--white);transform:rotate(-4deg)}

/* about */
.about-title{left:0;top:1413px;width:1200px;text-align:center;font-family:"Open Sans",sans-serif;font-size:30px;color:var(--blue)}
.about-text{left:235px;top:1466px;width:730px;text-align:center;font-size:13px;line-height:19px;color:var(--text-dark)}
.col{top:1562px;width:400px}
.col h2{font-family:"Open Sans",sans-serif;font-size:18px;color:var(--blue);margin-bottom:14px}
.col p{font-size:12px;line-height:16.5px;color:var(--text);text-align:justify;margin-bottom:16px}

/* blog + services */
.blue-band{left:0;top:1848px;width:1200px;height:383px;background:linear-gradient(180deg,#1c97e0,#1478c8)}
.band-title{top:1888px;font-family:"Open Sans",sans-serif;font-size:27px;color:var(--white)}
.blog-box{left:173px;top:1941px;width:627px;height:247px;background:var(--cream);border-radius:10px}
.post{position:absolute;top:24px;width:282px}
.post h4{font-size:11.5px;font-weight:700;color:var(--blue-dark);white-space:nowrap}
.post .meta{font-size:10px;color:#999;margin:3px 0 9px}
.post p{font-size:11px;line-height:15px;color:#6a5a2a}
.read-more{display:block;margin-top:8px;font-family:"Great Vibes",cursive;font-size:18px;color:#e2541a}
.dots{position:absolute;left:29px;top:224px}
.dots span{display:inline-block;width:9px;height:9px;border-radius:50%;background:var(--orange);margin-right:3px}
.services-box{left:822px;top:1941px;width:205px;height:247px;background:#0a5c98;border-radius:10px;padding:20px 0 0 24px}
.services-box li{list-style:none;font-size:11px;font-weight:700;color:var(--white);line-height:19.7px;position:relative;padding-left:20px}
.services-box li::before{content:"";position:absolute;left:0;top:5px;width:9px;height:9px;border-radius:50%;background:var(--white)}

/* footer */
.foot-h{top:2268px;font-family:"Open Sans",sans-serif;font-size:18px;color:var(--orange)}
.browse{left:173px;top:2312px;font-size:11px;line-height:17px;color:var(--text-dark);list-style:none}
.testi-photo{left:309px;top:2325px;width:66px;height:66px;border-radius:50%;background:linear-gradient(180deg,#c8a080,#6e5a48);border:3px solid #ddd}
.testi-quote{left:382px;top:2318px;width:268px;height:78px;background:#f2f2f2;border-radius:6px;padding:8px 10px;font-family:"Open Sans",sans-serif;font-style:italic;font-size:10.5px;line-height:14px;color:#888}
.testi-sign{left:548px;top:2398px;font-family:"Great Vibes",cursive;font-size:15px;color:var(--orange)}
.contact-row{left:666px;width:200px;font-size:11px;line-height:14px;color:#666}
.contact-ic{position:absolute;left:0;top:0;width:22px;height:22px}
.contact-row .txt{margin-left:32px}
.cta{left:860px;top:2300px;width:200px;height:120px}
.cta-strip{position:absolute;left:0;top:0;width:22px;height:120px;background:var(--orange);color:var(--white);font-size:11px;font-weight:700;writing-mode:vertical-rl;transform:rotate(180deg);text-align:center;letter-spacing:2px}
.cta-free{position:absolute;left:28px;top:-12px;font-family:"Open Sans",sans-serif;font-size:58px;color:var(--orange);line-height:64px}
.cta-sub{position:absolute;left:30px;top:52px;font-family:"Open Sans",sans-serif;font-size:19px;color:var(--orange)}
.cta-phone{position:absolute;left:28px;top:76px;font-family:"Open Sans",sans-serif;font-size:29px;color:var(--orange)}
.bottom-bar{left:0;top:2454px;width:1200px;height:141px;background:var(--footer-bg);border-top:1px solid #ddd}
.bottom-logo{left:0;top:2484px;width:1200px;text-align:center;font-family:"Open Sans",sans-serif;font-weight:600;font-size:18px;letter-spacing:3px;color:#aaa}
.bottom-links{left:0;top:2538px;width:1200px;text-align:center;font-size:11px;color:#777}
</style>
</head>
<body>

<div class="abs topline"></div>
<header class="abs site-header">
  <a class="abs nav-item" style="left:184px">Home</a>
  <a class="abs nav-item active" style="left:265px">About</a>
  <a class="abs nav-item" style="left:354px">Services</a>
  <a class="abs nav-item" style="left:450px">RFQ</a>
  <a class="abs nav-item" style="left:721px">Portfolio</a>
  <a class="abs nav-item" style="left:831px">Testimonials</a>
  <a class="abs nav-item" style="left:960px">Contact</a>
  <div class="abs nav-active-bar"></div>
</header>
<div class="abs logo-tab"><div class="logo-name">HURNLATE</div></div>

<section class="abs hero" role="img" aria-label="Sunset field photograph with a laptop, tablet, monitor and phone showing website designs"></section>
<svg class="abs hero-arrow" style="left:174px;top:298px" viewBox="0 0 62 62"><path d="M35 22 L26 31 L35 40" fill="none" stroke="#fff" stroke-width="3"/></svg>
<svg class="abs hero-arrow" style="left:964px;top:298px" viewBox="0 0 62 62"><path d="M27 22 L36 31 L27 40" fill="none" stroke="#fff" stroke-width="3"/></svg>

<h1 class="abs intro-title">70% of US households use the internet when searching for local products and services.</h1>
<p class="abs intro-text">While most purchases are made offline (67%), they start online at the businesses website. If your website looks unprofessional or cannot be found you are missing out on potential revenue and a steady stream of new customers.</p>

<div class="abs card card-yellow"><h3>Ecommerce</h3><div class="card-art" role="img" aria-label="Collage of online store pages"></div></div>
<div class="abs card card-orange"><h3>Web Design</h3><div class="card-art" role="img" aria-label="Collage of website layouts"></div></div>
<div class="abs card card-blue"><h3>Search Marketing</h3><div class="card-art" role="img" aria-label="Collage of search result pages"></div></div>

<section class="abs portfolio"></section>
<h2 class="abs portfolio-title">OUR PORTFOLIO</h2>
<svg class="abs hero-arrow" style="left:90px;top:1058px;width:56px;height:56px" viewBox="0 0 62 62"><path d="M35 22 L26 31 L35 40" fill="none" stroke="#fff" stroke-width="3"/></svg>
<svg class="abs hero-arrow" style="left:1053px;top:1058px;width:56px;height:56px" viewBox="0 0 62 62"><path d="M27 22 L36 31 L27 40" fill="none" stroke="#fff" stroke-width="3"/></svg>
<div class="abs portfolio-item" style="left:173px" role="img" aria-label="Dance studio website shown on a desktop computer"></div>
<div class="abs portfolio-item" style="left:465px;background:linear-gradient(180deg,#f6e46e,#d9d9d9)" role="img" aria-label="Tree and lawn service website shown on a desktop computer"></div>
<div class="abs portfolio-item" style="left:757px;background:linear-gradient(180deg,#b89a72,#d9d9d9)" role="img" aria-label="Restaurant website shown on a desktop computer"></div>
<a class="abs view-all">View All</a>
<div class="abs view-all-line"></div>

<h2 class="abs about-title">Hurnlate Website Design - PA</h2>
<p class="abs about-text">Hurnlate, a leading professional web design and web development company operating out of Carbonridge county in northeastern Pennsylvania, serves businesses everywhere from down the street to across the country.</p>

<div class="abs col" style="left:173px">
  <h2>What Makes Hurnlate Unique?</h2>
  <p>In a single word...results. Having a website that can't be found is equivalent to putting up a billboard facing away from traffic.</p>
  <p>An attractive site simply isn't enough in today's marketplace. So although many talented graphic designers can construct beautiful sites for pennies on the dollar, very few truly understand the principals of website marketing, copy and design, search engine optimization and legitimate tactics you can use so your website is found by your customers. With Hurnlate, you can have it all – an attractive site from talented designers and writers that achieves your business goals.</p>
</div>
<div class="abs col" style="left:627px">
  <h2>How Does Hurnlate Achieve Results?</h2>
  <p>In a single word...results. Having a website that can't be found is equivalent to putting up a billboard facing away from traffic.</p>
  <p>An attractive site simply isn't enough in today's marketplace. So although many talented graphic designers can construct beautiful sites for pennies on the dollar, very few truly understand the principals of website marketing, copy and design, search engine optimization and legitimate tactics you can use so your website is found by your customers. With Hurnlate, you can have it all – an attractive site from talented designers and writers that achieves your business goals.</p>
</div>

<section class="abs blue-band"></section>
<h2 class="abs band-title" style="left:199px">Recent Blog Postings</h2>
<h2 class="abs band-title" style="left:848px">Services</h2>
<div class="abs blog-box">
  <article class="post" style="left:29px">
    <h4>Making Your Website Work For You.</h4>
    <div class="meta">by Marcus on May 1, 2013</div>
    <p>Hey! Hope you are having an awesome day! Yesterday I was doing some follow up emails to potential clients that made contact with us sometime ago to see if there might some interest to work with each other yet. This one in particular that I emailed, I noticed that they did have a new website since our last contact and that it definitely did look better from what I remembered.</p>
    <a class="read-more">Read more →</a>
  </article>
  <article class="post" style="left:325px">
    <h4>Carbonridge Visitors Bureau Mobile Website Live Today</h4>
    <div class="meta">by Marcus on April 24, 2013</div>
    <p>Hey! Hope you are having an awesome day! Yesterday I was doing some follow up emails to potential clients that made contact with us sometime ago to see if there might some interest to work with each other yet. This one in particular that I emailed, I noticed that they did have a new website since our last contact and that it definitely did look better from what I remembered.</p>
    <a class="read-more">Read more →</a>
  </article>
  <div class="dots"><span></span><span style="background:#e2541a"></span><span></span><span></span><span></span></div>
</div>
<ul class="abs services-box">
  <li>Website Design</li><li>Website Re-design</li><li>Ecommerce</li><li>Mobile Websites</li><li>Copywriting</li><li>Hosting and Maintenance</li><li>Content Marketing</li><li>Pay Per Click Marketing</li><li>Mobile Text Marketing</li><li>Local Search Marketing</li>
</ul>

<h3 class="abs foot-h" style="left:173px">Browse Site</h3>
<ul class="abs browse"><li>Hurnlate</li><li>Services</li><li>Portfolio</li><li>Contact Us</li><li>Request A Quote</li><li>Associates</li></ul>
<h3 class="abs foot-h" style="left:309px">Client Testimonials</h3>
<div class="abs testi-quote">After finding our how hard you worked to develop our website I had to drop you a quick thank you note of true, heart felt thanks from the team and myself. We at The Amsel Group are proud to say....</div>
<div class="abs testi-photo" role="img" aria-label="Client portrait"></div>
<div class="abs testi-sign">R. Dale Amsel</div>
<h3 class="abs foot-h" style="left:666px">Contact Us</h3>
<div class="abs contact-row" style="top:2312px"><svg class="contact-ic" viewBox="0 0 22 22"><circle cx="11" cy="11" r="11" fill="#f39a1d"/><path d="M11 5a4 4 0 0 0-4 4c0 3 4 8 4 8s4-5 4-8a4 4 0 0 0-4-4z" fill="#fff"/></svg><div class="txt"><b>Hurnlate Web Design</b><br><i>12 Larkmoor Street<br>Eastvale, PA 17000</i></div></div>
<div class="abs contact-row" style="top:2366px"><svg class="contact-ic" viewBox="0 0 22 22"><circle cx="11" cy="11" r="11" fill="#f39a1d"/><path d="M8 6l2 3-1.5 1.5a7 7 0 0 0 3 3L13 12l3 2-1 2c-4 0-9-5-9-9z" fill="#fff"/></svg><div class="txt" style="color:var(--blue-dark);font-weight:700">(800) 555-0142<br>(570) 555-0189</div></div>
<div class="abs contact-row" style="top:2404px"><svg class="contact-ic" viewBox="0 0 22 22"><circle cx="11" cy="11" r="11" fill="#f39a1d"/><rect x="6" y="7.5" width="10" height="7" fill="#fff"/><path d="M6 7.5l5 4 5-4" fill="none" stroke="#f39a1d"/></svg><div class="txt" style="padding-top:4px">contact@hurnlatewd.example</div></div>
<div class="abs cta">
  <div class="cta-strip">CALL NOW</div>
  <div class="cta-free">FREE</div>
  <div class="cta-sub">CONSULTATION</div>
  <div class="cta-phone">570.555.0189</div>
</div>

<footer class="abs bottom-bar"></footer>
<div class="abs bottom-logo">HURNLATE</div>
<nav class="abs bottom-links">Hurnlate &nbsp;/&nbsp; Services &nbsp;/&nbsp; Portfolio &nbsp;/&nbsp; Contact Us &nbsp;/&nbsp; Request A Quote &nbsp;/&nbsp; Associates</nav>

</body>
</html>
```